Spring Style Exclusive Shopping Party for women

We need a postcard design for our Spring Shopping Event. Willow Lane is a women's apparel and accessories store featuring missy, petite and plus sizes. Event is Saturday, April 1 from 9am-10am. Looking for a twist on the spring shopping party idea. Attaching 2 postcards we have previously sent for this event and 2 ideas for what we are looking for in new postcard.

Target Market(s)

women 20+

Industry/Entity Type

Retail

Font styles to use
Serif

Requirements
Must have
• must be eye catching, have the logo, date and time of event,
Nice to have
• woman model

```html
<!DOCTYPE html>
<html lang="en">
<head>
<meta charset="utf-8">
<title>Willow Lane – Spring Shopping Party</title>
<link rel="stylesheet" href="https://fonts.googleapis.com/css2?family=Cormorant+Garamond:ital,wght@1,500&family=EB+Garamond:wght@400;500&family=Josefin+Sans:wght@400&display=swap">
<style>
  :root {
    --paper: #ffffff;
    --ink: #1d1d1d;
    --blush: #e0767c;
    --petal: #f4b9b4;
    --petal-soft: rgba(244, 170, 165, 0.55);
    --stem: rgba(60, 60, 60, 0.14);
  }
  html, body {
    margin: 0;
    padding: 0;
    width: 1200px;
    height: 928px;
    overflow: hidden;
    background: var(--paper);
  }
  .postcard {
    position: relative;
    width: 1200px;
    height: 928px;
    background: var(--paper);
    overflow: hidden;
  }
  .floral {
    position: absolute;
    border-radius: 50%;
  }
  .floral--top-left {
    left: -120px; top: -110px; width: 480px; height: 560px;
    background: radial-gradient(ellipse at 60% 45%, var(--petal-soft) 0%, var(--stem) 45%, rgba(255,255,255,0) 72%);
  }
  .floral--bottom-left {
    left: -140px; top: 560px; width: 520px; height: 480px;
    background: radial-gradient(ellipse at 40% 55%, var(--petal-soft) 0%, var(--stem) 45%, rgba(255,255,255,0) 72%);
  }
  .floral--top-right {
    left: 880px; top: -80px; width: 440px; height: 560px;
    background: radial-gradient(ellipse at 50% 45%, var(--petal-soft) 0%, var(--stem) 45%, rgba(255,255,255,0) 72%);
  }
  .floral--bottom-right {
    left: 780px; top: 560px; width: 520px; height: 460px;
    background: radial-gradient(ellipse at 50% 65%, var(--petal-soft) 0%, var(--stem) 45%, rgba(255,255,255,0) 72%);
  }
  .invite {
    position: absolute;
    left: 0;
    width: 1200px;
    text-align: center;
    color: var(--ink);
  }
  .invite__lead {
    top: 126px;
    font-family: "EB Garamond", serif;
    font-size: 31px;
  }
  .invite__season {
    position: absolute;
    left: 300px;
    top: 262px;
    margin: 0;
    font-family: "Cormorant Garamond", serif;
    font-style: italic;
    font-weight: 500;
    font-size: 84px;
    line-height: 1;
    color: var(--blush);
  }
  .invite__title {
    top: 332px;
    margin: 0;
    font-family: "Josefin Sans", sans-serif;
    font-weight: 400;
    font-size: 98px;
    line-height: 1;
    font-variant: small-caps;
    letter-spacing: 2px;
  }
  .invite__date {
    top: 484px;
    font-family: "EB Garamond", serif;
    font-size: 36px;
  }
  .divider {
    position: absolute;
    left: 260px;
    top: 552px;
  }
  .brand {
    top: 660px;
    font-family: "EB Garamond", serif;
    font-weight: 500;
    font-size: 62px;
    line-height: 1;
    color: var(--ink);
  }
  .brand__web {
    top: 768px;
    font-family: "EB Garamond", serif;
    font-size: 16px;
    letter-spacing: 2px;
  }
</style>
</head>
<body>
<main class="postcard">
  <div class="floral floral--top-left" role="img" aria-label="Hand-drawn leafy vine with pink watercolour blossoms"></div>
  <div class="floral floral--bottom-left" role="img" aria-label="Hand-drawn leafy vine with a peach watercolour blossom"></div>
  <div class="floral floral--top-right" role="img" aria-label="Hand-drawn branch with pink cherry blossoms"></div>
  <div class="floral floral--bottom-right" role="img" aria-label="Hand-drawn vine with peach watercolour blossoms"></div>

  <p class="invite invite__lead" style="margin:0">You are invited to our</p>
  <p class="invite__season">spring</p>
  <h1 class="invite invite__title">Shopping Party</h1>
  <p class="invite invite__date" style="margin:0">Saturday, April 1 from 9am-10am</p>

  <svg class="divider" width="730" height="24" viewBox="0 0 730 24" aria-hidden="true">
    <line x1="12" y1="12" x2="718" y2="12" stroke="var(--blush)" stroke-width="3"/>
    <circle cx="12" cy="12" r="11" fill="var(--blush)"/>
    <circle cx="718" cy="12" r="11" fill="var(--blush)"/>
  </svg>

  <p class="invite brand" style="margin:0">Willow Lane</p>
  <p class="invite brand__web" style="margin:0">www.willowlaneshop.com</p>
</main>
</body>
</html>
```